Quill Forge Solutions
Bold and Unique
Project: Quill Forge Solutions
Quill Forge Solutions -
Creative Brief
Simple
Gary Holbrook
Owner / IT Consultant
Gary@TheQuillForge.com
www.TheQuillForge.com
Please use either black and white, or black and red if you can... but if you find something that works better, than that works too!! Please be as creative and bold as possible!

```html
<!DOCTYPE html>
<html lang="en">
<head>
<meta charset="utf-8">
<title>Quill Forge Solutions — Business Card</title>
<link rel="stylesheet" href="https://fonts.googleapis.com/css2?family=Arimo:wght@400;700&family=Michroma&display=swap">
<style>
  :root {
    --ink: #111111;
    --paper: #ffffff;
    --frame: #3a3a3a;
    --red: #e41e26;
    --red-deep: #a8121b;
    --peach: #f6b193;
    --coral: #ee5a3c;
    --silver: #e9e9e9;
  }
  html, body {
    margin: 0;
    padding: 0;
    width: 1200px;
    height: 763px;
    overflow: hidden;
    background: var(--paper);
  }
  .canvas {
    position: relative;
    width: 1200px;
    height: 763px;
    overflow: hidden;
    background: var(--paper);
  }
  .card {
    position: absolute;
    left: 34px;
    top: 43px;
    width: 1152px;
    height: 682px;
    box-sizing: border-box;
    border: 2px solid var(--frame);
    background: var(--paper);
    overflow: hidden;
    font-family: "Arimo", Arial, sans-serif;
  }
  .card__wave {
    position: absolute;
    inset: 0;
    width: 100%;
    height: 100%;
  }
  .brand {
    position: absolute;
    left: 540px;
    top: 70px;
    width: 560px;
    text-align: center;
    color: var(--paper);
    font-family: "Michroma", "Arial Black", sans-serif;
    font-weight: 400;
  }
  .brand__dot {
    display: block;
    width: 130px;
    height: 130px;
    margin: 0 auto 26px;
    border-radius: 50%;
    background: var(--silver);
  }
  .brand__name {
    margin: 0;
    font-size: 50px;
    letter-spacing: 4px;
    line-height: 1;
  }
  .brand__sub {
    margin: 14px 0 0;
    font-size: 19px;
    letter-spacing: 9px;
    line-height: 1;
  }
  .tagline {
    position: absolute;
    left: 740px;
    top: 500px;
    width: 360px;
    margin: 0;
    text-align: center;
    color: var(--paper);
    font-weight: 700;
    font-size: 30px;
    line-height: 48px;
  }
  .person {
    position: absolute;
    left: 96px;
    top: 318px;
  }
  .person__name {
    margin: 0;
    font-weight: 700;
    font-size: 44px;
    color: var(--ink);
    line-height: 1.05;
  }
  .person__role {
    margin: 2px 0 0;
    font-weight: 700;
    font-size: 29px;
    color: var(--red);
  }
  .contacts {
    position: absolute;
    left: 100px;
    top: 452px;
    margin: 0;
    padding: 0;
    list-style: none;
  }
  .contacts__item {
    display: flex;
    align-items: center;
    height: 49px;
    font-weight: 700;
    font-size: 30px;
    color: var(--ink);
  }
  .contacts__icon {
    width: 26px;
    height: 26px;
    margin-right: 16px;
    flex: none;
  }
</style>
</head>
<body>
<div class="canvas">
  <div class="card">
    <svg class="card__wave" viewBox="0 0 1148 678" preserveAspectRatio="none" aria-hidden="true">
      <defs>
        <linearGradient id="waveFill" x1="0" y1="0" x2="1" y2="0.6">
          <stop offset="0" stop-color="#fde3d6"/>
          <stop offset="0.2" stop-color="var(--peach)"/>
          <stop offset="0.42" stop-color="var(--coral)"/>
          <stop offset="0.62" stop-color="var(--red)"/>
          <stop offset="1" stop-color="var(--red-deep)"/>
        </linearGradient>
      </defs>
      <path d="M0,0 H1148 V678 H752 C710,520 600,370 440,300 C330,250 150,210 0,175 Z" fill="url(#waveFill)"/>
    </svg>

    <div class="brand">
      <span class="brand__dot"></span>
      <p class="brand__name">QUILL FORGE</p>
      <p class="brand__sub">SOLUTIONS</p>
    </div>

    <p class="tagline">Clarity &amp; Strength<br>in Every Build</p>

    <div class="person">
      <h1 class="person__name">Gary Holbrook</h1>
      <p class="person__role">Owner/IT Consultant</p>
    </div>

    <ul class="contacts">
      <li class="contacts__item">
        <svg class="contacts__icon" viewBox="0 0 24 24" aria-hidden="true">
          <path fill="var(--red)" d="M6.6 10.8c1.4 2.8 3.8 5.1 6.6 6.6l2.2-2.2c.3-.3.7-.4 1-.2 1.1.4 2.300.6 3.6.6.6 0 1 .4 1 1V20c0 .6-.4 1-1 1C10.6 21 3 13.4 3 4c0-.6.4-1 1-1h3.5c.6 0 1 .4 1 1 0 1.3.2 2.5.6 3.6.1.3 0 .7-.2 1z"/>
        </svg>
        <span>5550142398</span>
      </li>
      <li class="contacts__item">
        <svg class="contacts__icon" viewBox="0 0 24 24" aria-hidden="true">
          <rect x="2" y="5" width="20" height="14" fill="var(--red)"/>
          <path d="M2.5 5.5 L12 13 L21.5 5.5" fill="none" stroke="var(--paper)" stroke-width="1.8"/>
        </svg>
        <span>Gary@TheQuillForge.com</span>
      </li>
      <li class="contacts__item">
        <svg class="contacts__icon" viewBox="0 0 24 24" aria-hidden="true">
          <g fill="none" stroke="var(--red)" stroke-width="2">
            <circle cx="12" cy="12" r="9.5"/>
            <ellipse cx="12" cy="12" rx="4" ry="9.5"/>
            <path d="M2.5 12 H21.5 M4 7 H20 M4 17 H20"/>
          </g>
        </svg>
        <span>www.TheQuillForge.com</span>
      </li>
    </ul>
  </div>
</div>
</body>
</html>
```